Vimbo. Packaging for mood-boosting energy drink mix. Upbeat and uplifting.

I need a mockup of a pouch package + a stick. I included an image of a Crest Flow pouch + stick for reference. I do not have a die line for the pouch, so feel free to just use the same relative dimensions for the pouch and create a rendering. Here are the specifications for the packaging that I need:
1. The logo is included in the uploaded files. Please use the one that says "feel good energy" beneath "vimbo." The logo should take up about the top 1/3 to 1/2 of the pouch.
2. The pouch should be mostly white, especially behind the logo, but feel free to explore yellow or orange for the bottom 1/2 to 2/3 of the packaging.
3. In the center of the packaging, below the logo, please have the product name appear, "mood-boosting energy drink mix" similar to where "Thirst Amplifier" is placed.
4. Below that, create an image of a glass with a stick pouring into it like in the Crest Flow pouch.
5. Below the glass, in the bottom center of the package, include "16 sticks. Net Wt. 4 oz. (114 g)
6. On the left side, please include callouts, from top to bottom, "energy blend (80mg caffeine, taurine) + happy blend (saffron, st. john's wort, rhodiola).
7. On the right side, please include callouts, from top to bottom, "electrolytes + vitamins + 0g sugar"
8. Somewhere else on the front of the packaging, please include the flavor name "golden berry," perhaps where they do on the crest flow pouch.
9. For the stick, use your creativity.
10. There is no back of packaging to design for this project.

Target Market(s)

My target consumer leads a very active lifestyle and cares deeply about health & wellness.

Colors
0094D4
00A9DD
6FCCEA
C7EBF8
E9F6FB
FFC000
F8CF3A
FAE287
FDF2CF
FEFAEE
F0912C
F2A743
F7CA91
FBE8D2
FDF5EE
EE7325
F08F49
F5BC92
FAE3D3
FDF4ED

Requirements
Must have
• My packaging must make people feel good and maybe even smile when they see it. A brand that does this well is Pemba. (www.pemba-example.com)
Nice to have
• I like 60's Mod Design if you need some inspiration. The packaging should also convey a sense of levity. Like you'll float or dance through life after drinking this.

```html
<!DOCTYPE html>
<html lang="en">
<head>
<meta charset="utf-8">
<title>Vimbo – Mood-Boosting Energy Drink Mix Packaging</title>
<link rel="stylesheet" href="https://fonts.googleapis.com/css2?family=Oswald:wght@300;400;500&family=Varela+Round&display=swap">
<style>
  :root {
    --blue: #00A9DD;
    --blue-light: #6FCCEA;
    --yellow: #FFC000;
    --yellow-soft: #F8CF3A;
    --yellow-pale: #FAE287;
    --orange: #F0912C;
    --orange-mid: #F2A743;
    --orange-deep: #EE7325;
    --orange-light: #F5BC92;
    --cream: #F4F1EC;
    --white: #FFFFFF;
    --backdrop: #F7F7F7;
  }
  * { box-sizing: border-box; margin: 0; padding: 0; }
  html, body { width: 1200px; height: 675px; overflow: hidden; }
  body {
    background: var(--backdrop);
    position: relative;
    font-family: "Oswald", sans-serif;
  }

  /* ---------- Pouch ---------- */
  .pouch {
    position: absolute;
    left: 329px; top: 81px;
    width: 408px; height: 535px;
    background: var(--cream);
    border-radius: 4px 4px 10px 10px;
    overflow: hidden;
  }
  .pouch__claim {
    position: absolute; left: 41px; top: 20px;
    color: var(--orange);
  }
  .pouch__claim-main {
    display: block; font-size: 21px; font-weight: 400; letter-spacing: 0.5px; line-height: 1;
  }
  .pouch__claim-sub {
    display: block; font-family: "Varela Round", sans-serif; font-style: italic;
    font-size: 12px; margin-top: 2px;
  }
  .pouch__count {
    position: absolute; left: 300px; top: 46px; width: 108px; height: 40px;
    background: var(--blue);
    clip-path: polygon(0 0, 100% 0, 100% 100%, 0 100%, 9% 50%);
    color: var(--white);
    display: flex; align-items: center; padding-left: 22px; gap: 5px;
  }
  .pouch__count-num { font-size: 28px; line-height: 1; }
  .pouch__count-label { font-size: 11px; line-height: 1.05; }

  .brand { position: absolute; text-align: right; color: var(--orange-deep); font-family: "Varela Round", sans-serif; }
  .pouch .brand { left: 100px; top: 100px; width: 205px; }
  .brand__name { display: block; font-size: 86px; line-height: 1; letter-spacing: -2px; }
  .brand__tagline { display: block; font-size: 13px; margin-top: -4px; }

  .pattern-band {
    position: absolute; left: 0; right: 0;
    background: repeating-linear-gradient(90deg,
      var(--yellow) 0 13px, var(--orange-mid) 13px 26px,
      var(--blue-light) 26px 39px, var(--orange) 39px 52px);
  }
  .pouch .pattern-band--top { top: 218px; height: 34px; }
  .pouch .pattern-band--bottom { top: 499px; height: 36px; }

  .pouch__panel {
    position: absolute; left: 0; right: 0; top: 252px; height: 247px;
    background: radial-gradient(circle at 50% 55%, var(--orange-mid) 0%, var(--orange) 70%);
  }
  .pouch__product {
    position: absolute; left: 0; right: 0; top: 266px;
    text-align: center; color: var(--white);
    font-size: 24px; font-weight: 400; letter-spacing: -0.3px;
  }
  .callout {
    position: absolute; display: flex; flex-direction: column; justify-content: center;
    align-items: center; text-align: center;
    background: var(--yellow-soft); color: var(--orange);
    font-weight: 300; line-height: 1.25;
  }
  .callout--left { clip-path: polygon(0 0, 90% 0, 100% 50%, 90% 100%, 0 100%); padding-right: 14px; font-size: 9.5px; }
  .callout--right { clip-path: polygon(8% 0, 100% 0, 100% 100%, 8% 100%, 0 50%); padding-left: 10px; font-size: 12px; }
  .callout__title { font-size: 10px; }

  .pouch__glass {
    position: absolute; left: 166px; top: 345px; width: 82px; height: 82px;
    border-radius: 50%;
    background: radial-gradient(circle, var(--blue-light) 0 22%, var(--orange-deep) 23%);
  }
  .flavor {
    position: absolute; background: var(--blue); color: var(--white);
    border-radius: 20px; display: flex; align-items: center; justify-content: center;
    font-weight: 400;
  }
  .pouch .flavor { left: 63px; top: 465px; width: 70px; height: 22px; font-size: 10px; }
  .pouch__weight {
    position: absolute; left: 267px; top: 465px; color: var(--white);
    font-size: 11px; font-weight: 300;
  }

  /* ---------- Stick ---------- */
  .stick {
    position: absolute; left: 792px; top: 185px; width: 98px; height: 419px;
    background: var(--cream); overflow: hidden; border-radius: 2px;
  }
  .stick__tear {
    position: absolute; left: 6px; top: 13px; font-family: "Varela Round", sans-serif;
    font-size: 7.5px; color: var(--orange);
  }
  .stick__perforation {
    position: absolute; left: 0; right: 0; top: 28px; border-top: 1px dashed var(--orange-light);
  }
  .stick .brand { left: 0; right: 0; top: 40px; text-align: center; }
  .stick .brand__name { font-size: 32px; letter-spacing: -1px; }
  .stick__tagline {
    position: absolute; left: 0; right: 0; top: 92px; text-align: center;
    font-family: "Varela Round", sans-serif; font-size: 15px; line-height: 1.15; color: var(--orange);
  }
  .stick__panel {
    position: absolute; left: 0; right: 0; top: 159px; bottom: 0;
    background: linear-gradient(var(--orange-mid), var(--orange));
  }
  .stick__badge {
    position: absolute; left: 2px; top: 159px; width: 94px; height: 94px; border-radius: 50%;
    background: var(--orange-deep);
  }
  .stick__product {
    position: absolute; left: 0; right: 0; top: 189px; text-align: center;
    color: var(--white); font-size: 12px; line-height: 1.25;
  }
  .stick__benefits {
    position: absolute; left: 0; right: 0; top: 280px; text-align: center;
    color: var(--yellow-soft); font-size: 11px; line-height: 1.62; font-weight: 300;
    list-style: none;
  }
  .stick .flavor { left: 13px; top: 348px; width: 76px; height: 19px; font-size: 8.5px; }
  .stick__weight {
    position: absolute; left: 0; right: 0; top: 380px; text-align: center;
    color: var(--white); font-size: 8.5px; font-weight: 300;
  }
</style>
</head>
<body>

  <section class="pouch" aria-label="Vimbo pouch front">
    <p class="pouch__claim">
      <span class="pouch__claim-main">IMPROVE</span>
      <span class="pouch__claim-sub">your mood easily</span>
    </p>
    <div class="pouch__count"><span class="pouch__count-num">6</span><span class="pouch__count-label">STICK<br>PACKS</span></div>

    <div class="brand">
      <span class="brand__name">vimbo</span>
      <span class="brand__tagline">feel good energy</span>
    </div>

    <div class="pattern-band pattern-band--top" role="img" aria-label="Mod pattern band of semicircles in yellow, orange and blue"></div>
    <div class="pouch__panel"></div>
    <h1 class="pouch__product">MOOD-BOOSTING ENERGY DRINK MIX</h1>

    <div class="callout callout--left" style="left:0;top:324px;width:149px;height:46px;">
      <span class="callout__title">ENERGY BLEND</span><span>(80mg caffeine, taurine)</span>
    </div>
    <div class="callout callout--left" style="left:0;top:377px;width:149px;height:59px;">
      <span class="callout__title">HAPPY BLEND</span><span>(saffron, st. john's wort,<br>rhodiola)</span>
    </div>

    <div class="pouch__glass" role="img" aria-label="Illustration of a stick pack pouring powder into a glass of water"></div>

    <div class="callout callout--right" style="left:268px;top:324px;width:125px;height:33px;">ELECTROLYTES</div>
    <div class="callout callout--right" style="left:268px;top:364px;width:125px;height:33px;">VITAMINS</div>
    <div class="callout callout--right" style="left:268px;top:403px;width:125px;height:33px;">0G SUGAR</div>

    <div class="flavor">GOLDEN BERRY</div>
    <p class="pouch__weight">NET WT. 4 OZ. (114 G)</p>
    <div class="pattern-band pattern-band--bottom" role="img" aria-label="Mod pattern band of semicircles in yellow, orange and blue"></div>
  </section>

  <section class="stick" aria-label="Vimbo stick pack">
    <p class="stick__tear">Tear Here</p>
    <div class="stick__perforation"></div>
    <div class="brand"><span class="brand__name">vimbo</span></div>
    <p class="stick__tagline">Feel Good<br>Energy</p>
    <div class="stick__panel"></div>
    <div class="stick__badge"></div>
    <p class="stick__product">MOOD-BOOSTING<br>ENERGY DRINK MIX</p>
    <ul class="stick__benefits">
      <li>ELECTROLYTES</li>
      <li>VITAMINS</li>
      <li>0G SUGAR</li>
    </ul>
    <div class="flavor">GOLDEN BERRY</div>
    <p class="stick__weight">Net Wt. 4 oz. (114 g)</p>
  </section>

</body>
</html>
```